Market place for used airplanes/helicopters/parts

http://www.kvistbladet.se needs a facelift.

# What is it
Classifieds for used airplanes/helicopters/parts/spare parts/aviation literature, for people in Scandinavia. The number of classifieds is ~120-200. They are mainly in Swedish, English, Norwegian.

It's not a glamorous or luxurious business, but more for people with a genuine interest in flying, technical things.

Similar to sites like this, but they have much more classifieds than my site
http://www.trevoxlist.com/list/list.aspx?ETID=1&setype=1&catid=6
http://www.bergholmaircraft.com/planes.asp?meny=1&typ=single
https://www.quillhoppers.com/cat.php?mode=listing&main=

# What I want
Design only - no code. I want a modern, maybe a bit bootstrap like, clean, simple, not flashy, web design. I want the design to be in English.

# Audience of the website
Aviation interested men, 45-65 years old, in the nordic countries (around Sweden).

# Logotype that could be used (but not necessarily)
http://www.kvistbladet.se/flygplan_till_salu_large.jpg
http://www.kvistbladet.se/flygplan_till_salu.eps

Reason: I decided to extend the deadline with 1 day. The reason is that I (unfortunately) managed to put the contest in the wrong category for 1 day + I want to give you all feedback (been too busy the whole day, sorry).

Hi all! 

Thanks everyone for the contributions you made. 

I will setup a poll for the designs that I like most. Will get back when I have more information. 

Thanks and have a nice weekend!
Lev

45-65 old Scandinavian men

Business

• - A list with classifieds on the first page, so the visitor easily can see new classifieds.
- A classifieds should be able to have more than one photo
- A simple navigation for showing classifieds from categories like airplanes, helicopters/gyrocopters, parts, literature, misc (maybe other categories) .... but still, it's just 100-200 ads so it's not needed that much filtration.

- A placeholder/way of showing aviation news/clips. In the old design I had, it was a column to the right. It's enough to show maybe 2-5 placeholders.
- A placeholder for PlinkAds ads somewhere on the site.
• - Carousels
- Too much clutter

```html
<!DOCTYPE html>
<html lang="en">
<head>
<meta charset="utf-8">
<title>Luftmarknad – Classifieds</title>
<link href="https://fonts.googleapis.com/css2?family=Montserrat:wght@400;500;600;700&display=swap" rel="stylesheet">
<style>
:root{
  --page-bg:#e9eaec;
  --card:#ffffff;
  --brand:#1f4e96;
  --brand-bright:#1b7fc4;
  --text:#2f2f2f;
  --muted:#9a9a9a;
  --nav:#3a3b3d;
  --nav-line:#55575a;
  --border:#d4d4d4;
  --ad:#939393;
  --placeholder:#ececec;
}
*{box-sizing:border-box;margin:0;padding:0}
html,body{width:1200px;height:788px;overflow:hidden}
body{background:linear-gradient(#dcdde0,var(--page-bg) 30%,#f1f1f2);font-family:"Montserrat",Arial,sans-serif;color:var(--text);position:relative}
.site-card{position:absolute;left:264px;top:20px;width:671px;height:726px;background:var(--card)}
.brand{position:absolute;left:15px;top:26px;display:flex;align-items:center;gap:8px}
.brand-mark{width:12px;height:12px;background:var(--brand)}
.brand-name{font-weight:700;font-size:20px;color:var(--brand);letter-spacing:.5px}
.search{position:absolute;left:506px;top:33px;width:152px;height:20px;background:var(--brand-bright);border:1px solid var(--brand);display:flex;align-items:center;padding:2px}
.search-input{flex:1;height:14px;background:#fff;border:1px solid #0f5c95}
.search-btn{font-size:7px;font-weight:700;color:#fff;padding:0 5px;letter-spacing:.2px}
.hero{position:absolute;left:12px;top:75px;width:646px;height:124px;background:linear-gradient(180deg,#8a8fa6 0%,#b7b8c6 45%,#8f9096 70%,#6f7076 100%)}
.hero-plane{position:absolute;right:60px;top:0;width:320px;height:124px;background:linear-gradient(160deg,#f3f5f8 0%,#dfe6ee 40%,#2a8ad0 75%,#1d6fb2 100%);opacity:.85}
.category-nav{position:absolute;left:12px;top:199px;width:646px;height:26px;background:var(--nav);display:flex;align-items:center;box-shadow:0 2px 2px rgba(0,0,0,.25)}
.nav-item{height:100%;display:flex;align-items:center;gap:5px;padding:0 8px;border-right:1px solid var(--nav-line);color:#fff;font-size:7.5px;font-weight:700;letter-spacing:.2px}
.check{width:8px;height:8px;background:#fff;display:inline-block}
.nav-tools{margin-left:auto;display:flex;align-items:center;gap:5px;padding-right:6px;color:#fff;font-size:7.5px;font-weight:500}
.show-select{width:88px;height:14px;background:#fff;color:var(--text);font-size:7.5px;display:flex;align-items:center;justify-content:space-between;padding-left:5px;margin-right:14px}
.show-select .arrow{width:14px;height:14px;border-left:1px solid #ccc;display:flex;align-items:center;justify-content:center}
.view-btn{width:15px;height:15px}
.listing-box{position:absolute;left:12px;top:237px;width:646px;height:463px;border:1px solid var(--border)}
.ad{position:absolute;left:9px;top:9px;width:495px}
.ad-photo{position:absolute;left:0;top:0;width:155px;height:115px}
.ad-photo.real{background:linear-gradient(180deg,#8c8f95 0%,#5d6066 55%,#3e4044 100%)}
.ad-photo.empty,.ad-thumb.empty{background:var(--placeholder)}
.ad-thumb{position:absolute;left:161px;width:49px;height:36px}
.ad-thumb.real{background:linear-gradient(180deg,#7b7f86,#4d5055)}
.ad-body{position:absolute;left:226px;top:-3px;width:380px;font-size:8.7px;line-height:10.5px}
.ad-title{display:flex;align-items:baseline;gap:6px;margin-bottom:8px}
.ad-title h2{font-size:15px;font-weight:700;color:var(--brand);line-height:16px}
.ad-cat{font-size:7.5px;font-weight:500}
.ad-text p+p{margin-top:10.5px}
.sponsor{position:absolute;left:9px;width:626px;height:78px;background:var(--ad);color:#fff;font-weight:700;font-size:17px;letter-spacing:.5px;display:flex;align-items:center;justify-content:center}
.pagination{position:absolute;left:0;right:0;top:510px;display:flex;justify-content:center;gap:8px;font-size:7.5px;font-weight:500}
.pagination .off{color:#bbb}
.pagination .current{color:var(--brand);font-weight:700}
.footer{position:absolute;left:279px;top:760px;font-size:8px;font-weight:500;color:#444}
</style>
</head>
<body>
<div class="site-card">
  <header>
    <a class="brand"><span class="brand-mark"></span><span class="brand-name">LUFTMARKNAD</span></a>
    <div class="search"><span class="search-input"></span><span class="search-btn">SEARCH</span></div>
  </header>

  <div class="hero" role="img" aria-label="Photo of a blue and white high-wing aircraft parked on an airfield apron"><div class="hero-plane"></div></div>

  <nav class="category-nav">
    <span class="nav-item"><svg class="check" viewBox="0 0 8 8"><rect width="8" height="8" fill="#fff"/><path d="M1.5 4 3.3 5.8 6.6 1.8" fill="none" stroke="#1f4e96" stroke-width="1.4"/></svg>AIRPLANES</span>
    <span class="nav-item"><svg class="check" viewBox="0 0 8 8"><rect width="8" height="8" fill="#fff"/><path d="M1.5 4 3.3 5.8 6.6 1.8" fill="none" stroke="#1f4e96" stroke-width="1.4"/></svg>HELICOPTERS</span>
    <span class="nav-item"><span class="check"></span>PARTS</span>
    <span class="nav-item"><span class="check"></span>SPARE PARTS</span>
    <span class="nav-item"><span class="check"></span>AVIATION LITERATURE</span>
    <div class="nav-tools">
      <span>Show:</span>
      <span class="show-select">200 ads<span class="arrow"><svg width="6" height="4" viewBox="0 0 6 4"><path d="M0 0h6L3 4z" fill="#888"/></svg></span></span>
      <svg class="view-btn" viewBox="0 0 15 15"><g fill="#c9c9c9"><rect x="2" y="2" width="5" height="5"/><rect x="8" y="2" width="5" height="5"/><rect x="2" y="8" width="5" height="5"/><rect x="8" y="8" width="5" height="5"/></g></svg>
      <svg class="view-btn" viewBox="0 0 15 15"><rect x=".5" y=".5" width="14" height="14" fill="#fff" stroke="#999"/><g fill="#555"><rect x="2" y="2.5" width="4" height="4"/><rect x="7" y="3" width="6" height="1.5"/><rect x="2" y="8.5" width="4" height="4"/><rect x="7" y="9" width="6" height="1.5"/></g></svg>
    </div>
  </nav>

  <main class="listing-box">
    <article class="ad">
      <div class="ad-photo real" role="img" aria-label="Photo of a blue and white low-wing aircraft outside a hangar"></div>
      <div class="ad-thumb real" style="top:0" role="img" aria-label="Aircraft photo thumbnail"></div>
      <div class="ad-thumb real" style="top:39px" role="img" aria-label="Aircraft photo thumbnail"></div>
      <div class="ad-thumb real" style="top:79px" role="img" aria-label="Aircraft photo thumbnail"></div>
      <div class="ad-body">
        <div class="ad-title"><h2>VARDA6</h2><span class="ad-cat">AIRPLANES</span></div>
        <div class="ad-text">
          <p>Vi sonderar marknaden för vår UL klassade Varda, bygd 1997. Maskinen är i mycket gott skick. 1120tim totalt, 430tim på motor &amp; prop. Flottörfästen installerade.<br>350.000:-<br>Låter det intressant? skicka ett mail.</p>
          <p>Nils<br>Namn: Nils Bergqvist, E-posta<br>Telefon: 070-4418360<br>Datum: 2013-09-27 06:55:21</p>
        </div>
      </div>
    </article>
    <div class="sponsor" style="top:134px">PLINKADS</div>

    <article class="ad" style="top:223px">
      <div class="ad-photo empty" role="img" aria-label="No photo placeholder"></div>
      <div class="ad-thumb empty" style="top:0"></div>
      <div class="ad-thumb empty" style="top:39px"></div>
      <div class="ad-thumb empty" style="top:79px"></div>
      <div class="ad-body">
        <div class="ad-title"><h2>VARDA6</h2><span class="ad-cat">AIRPLANES</span></div>
        <div class="ad-text">
          <p>Vi sonderar marknaden för vår UL klassade Varda, bygd 1997. Maskinen är i mycket gott skick. 1120tim totalt, 430tim på motor &amp; prop. Flottörfästen installerade.<br>350.000:-<br>Låter det intressant? skicka ett mail.</p>
          <p>Nils<br>Namn: Nils Bergqvist, E-posta<br>Telefon: 070-4418360<br>Datum: 2013-09-27 06:55:21</p>
        </div>
      </div>
    </article>
    <div class="sponsor" style="top:351px">PLINKADS</div>

    <nav class="pagination" style="top:437px"><span class="off">« Previous</span><span class="current">1</span><span>2</span><span>Next »</span></nav>
  </main>
</div>
<footer class="footer">© 2013 LUFTMARKNAD</footer>
</body>
</html>
```